Postcard Design

Need postcard design for dental office. The doctor is returning to the office after a few months medical leave and he wants a postcard to be mailed to patients and families in the surrounding area to create new patients. We have attached a rough sketch of the information we would like to include on the postcard along with color selection but are open to additional artwork or design to improve the overall look. We are also including a photo of the dentist for the front of the postcard. We plan to have the metered postage through Plentomark if possible so please let me know how that works because I'm assuming that will need to be included in the design. I am also attaching a sample of a postcard that the dentist received in the mail from a Corbridge doctor and would like his postcard to resemble this layout. The postcard needs to 8.5 x 5.5; I believe this is called the oversized selection for Plentomark and we are planning to have them do the printing. Please verify you did receive four attached files including photo, front sketch, back sketch, and actual postcard example.

Thank you,
Marlene Tofsky

```html
<!DOCTYPE html>
<html lang="en">
<head>
<meta charset="utf-8">
<title>Dr. Neal Harbin – Postcard Back</title>
<link rel="stylesheet" href="https://fonts.googleapis.com/css2?family=Montserrat:wght@400;700&family=PT+Sans&family=Roboto+Condensed:wght@300;700&display=swap">
<style>
  :root {
    --navy-deep: #0b2342;
    --navy: #133764;
    --navy-mid: #1a4a80;
    --stripe: #1f95d3;
    --cyan-light: #9fe0f0;
    --white: #ffffff;
    --ink: #1c2f5a;
    --rule: #c9ccd1;
    --paper: #ffffff;
  }
  * { margin: 0; padding: 0; box-sizing: border-box; }
  html, body { width: 1200px; height: 789px; overflow: hidden; background: var(--paper); }
  .postcard { position: relative; width: 1200px; height: 789px; background: var(--paper); }

  .header-panel {
    position: absolute; left: 0; top: 0; width: 1035px; height: 428px;
    background: linear-gradient(180deg, var(--navy-deep) 0%, var(--navy) 60%, var(--navy-deep) 100%);
  }
  .brand-name {
    position: absolute; left: 36px; top: 40px;
    font-family: "Montserrat", sans-serif; font-weight: 400;
    font-size: 33px; color: var(--white); letter-spacing: 0.5px;
    display: flex; align-items: center; gap: 12px;
  }
  .brand-dot { width: 11px; height: 11px; border-radius: 50%; background: var(--stripe); }
  .headline {
    position: absolute; left: 555px; top: 36px;
    font-family: "Roboto Condensed", sans-serif; line-height: 1.0;
  }
  .headline-strong { display: block; font-weight: 700; font-size: 34px; color: var(--cyan-light); }
  .headline-light {
    display: block; margin-left: 131px; font-weight: 300; font-size: 34px;
    letter-spacing: 1.6px; color: var(--white);
  }
  .accent-stripe {
    position: absolute; left: 0; top: 140px; width: 1035px; height: 22px; background: var(--stripe);
  }
  .contact-row {
    position: absolute; left: 0; top: 162px; width: 1035px; height: 266px; display: flex;
  }
  .contact-cell {
    flex: 1; position: relative; display: flex; flex-direction: column; align-items: center;
  }
  .contact-cell--phone {
    background: linear-gradient(180deg, var(--navy-mid), var(--navy));
    border-left: 2px dashed rgba(255,255,255,.35);
    border-right: 2px dashed rgba(255,255,255,.35);
  }
  .contact-icon { margin-top: 28px; width: 136px; height: 136px; }
  .contact-text {
    margin-top: 20px; font-family: "Montserrat", sans-serif; font-weight: 700;
    font-size: 20px; line-height: 1.35; color: var(--white); text-align: center;
    white-space: nowrap;
  }
  .contact-text--single { margin-top: 33px; }

  .stamp-box {
    position: absolute; left: 1062px; top: 36px; width: 102px; height: 110px;
    border: 1px solid var(--rule);
  }
  .bio {
    position: absolute; left: 37px; top: 472px; width: 640px;
    font-family: "PT Sans", sans-serif; font-size: 23px; line-height: 1.42; color: var(--ink);
  }
  .bio p + p { margin-top: 30px; }
  .address-lines { position: absolute; left: 762px; top: 494px; width: 363px; }
  .address-line { height: 0; border-top: 2px solid var(--rule); margin-bottom: 51px; }
</style>
</head>
<body>
<div class="postcard">
  <section class="header-panel">
    <div class="brand-name"><span>DR. NEAL HARBIN</span><span class="brand-dot"></span></div>
    <div class="headline">
      <span class="headline-strong">ACCEPTING ESTABLISHED</span>
      <span class="headline-light">AND NEW PATIENTS</span>
    </div>
    <div class="accent-stripe"></div>
    <div class="contact-row">
      <div class="contact-cell contact-cell--address">
        <svg class="contact-icon" viewBox="0 0 136 136" aria-hidden="true">
          <defs><linearGradient id="iconFillA" x1="0" y1="0" x2="0" y2="1"><stop offset="0" stop-color="#4cc6f2"/><stop offset="1" stop-color="#0a78bf"/></linearGradient></defs>
          <circle cx="68" cy="68" r="66" fill="url(#iconFillA)"/>
          <path d="M68 30 L108 66 L99 66 L99 104 L78 104 L78 80 L58 80 L58 104 L37 104 L37 66 L28 66 Z" fill="#ffffff"/>
          <rect x="86" y="36" width="9" height="18" fill="#ffffff"/>
        </svg>
        <div class="contact-text">4820 Alder Ridge Rd. Suite 210<br>Maple Fork , GA 30418</div>
      </div>
      <div class="contact-cell contact-cell--phone">
        <svg class="contact-icon" viewBox="0 0 136 136" aria-hidden="true">
          <defs><linearGradient id="iconFillB" x1="0" y1="0" x2="0" y2="1"><stop offset="0" stop-color="#4cc6f2"/><stop offset="1" stop-color="#0a78bf"/></linearGradient></defs>
          <circle cx="68" cy="68" r="66" fill="url(#iconFillB)"/>
          <path d="M48 30 C40 32 34 40 36 52 C40 74 56 94 78 104 C88 108 98 104 102 96 L92 84 C89 81 85 81 82 84 L77 88 C66 81 58 72 53 60 L58 55 C61 52 61 48 59 45 Z" fill="#ffffff"/>
        </svg>
        <div class="contact-text contact-text--single">770-555-0182</div>
      </div>
      <div class="contact-cell contact-cell--web">
        <svg class="contact-icon" viewBox="0 0 136 136" aria-hidden="true">
          <defs><linearGradient id="iconFillC" x1="0" y1="0" x2="0" y2="1"><stop offset="0" stop-color="#4cc6f2"/><stop offset="1" stop-color="#0a78bf"/></linearGradient></defs>
          <circle cx="68" cy="68" r="66" fill="url(#iconFillC)"/>
          <g fill="none" stroke="#ffffff" stroke-width="6">
            <circle cx="68" cy="68" r="36"/>
            <ellipse cx="68" cy="68" rx="16" ry="36"/>
            <line x1="32" y1="68" x2="104" y2="68"/>
            <path d="M38 50 H98 M38 86 H98"/>
          </g>
        </svg>
        <div class="contact-text contact-text--single">drnealharbin.com</div>
      </div>
    </div>
  </section>

  <div class="stamp-box"></div>

  <section class="bio">
    <p>Neal R. Harbin DDS, FAGD a native of Maple Fork, GA,<br>Dr. Harbin earned his Doctorate of Dental Surgery at the<br>Cumberland State Dental School in Ashford.</p>
    <p>Dr. Harbin has been improving the dental health of<br>patients in Western Georgia for 25 years</p>
  </section>

  <div class="address-lines">
    <div class="address-line"></div>
    <div class="address-line"></div>
    <div class="address-line"></div>
    <div class="address-line"></div>
  </div>
</div>
</body>
</html>
```